Brightpath Learning Data Dashboard

Brightpath Learning is a leading provider of digital curriculum and online courses to increase educational opportunities and achievement to students in grades K-12. Teachers and students access all course materials online.

School districts need greater visibility into the rate in which students are progressing through their courses, so school staff can better support students to complete courses at the required rate to keep them on track for graduation.
This can be accomplished by allowing school administrators to view a data dashboard and pull an on-demand report and see progress for a specified date range, relative to overall progress.

Within a specified date range, school administrators want to know if the student made more or less progress than in the period prior to the first date in the range.
School administrators also want to know if students are ahead or behind where they should be after the second date in the range.

Industry/Entity Type

Digital

```html
<!DOCTYPE html>
<html lang="en">
<head>
<meta charset="utf-8">
<title>Education Data Dashboard</title>
<link href="https://fonts.googleapis.com/css2?family=Roboto:wght@400;500;700&display=swap" rel="stylesheet">
<style>
:root{
  --bg:#f4f8fc;
  --blue:#2196f3;
  --band:#d9ecfc;
  --white:#ffffff;
  --border:#cfd8e0;
  --text-blue:#1e88e5;
  --label:#222;
  --red:#c62828;
  --green:#1b7a1b;
  --dark:#222;
}
*{box-sizing:border-box;margin:0;padding:0}
html,body{width:1200px;height:686px;overflow:hidden}
body{background:var(--bg);font-family:"Roboto",Arial,sans-serif;position:relative}
.page-title{position:absolute;top:9px;left:0;width:1138px;text-align:center;font-size:23px;font-weight:400;color:var(--blue);letter-spacing:.3px}

/* filters */
.filters{position:absolute;left:14px;top:70px;width:117px}
.field{position:absolute;left:0;width:117px;height:24px;border:1px solid var(--border);background:var(--white);padding:4px 3px}
.field-inner{height:100%;border:1px solid #9aa8b4;font-size:5.5px;color:#444;display:flex;align-items:center;justify-content:space-between;padding:0 4px}
.caret{width:0;height:0;border-left:3px solid transparent;border-right:3px solid transparent;border-top:3px solid var(--blue)}
.filter-label{position:absolute;left:4px;font-size:7.5px;font-weight:400;color:var(--label);letter-spacing:.3px}
.radios{position:absolute;left:1px;top:80px;font-size:7.5px;font-weight:400;color:var(--label);display:flex;gap:8px;align-items:center}
.radio{display:flex;align-items:center;gap:3px}
.dot{width:7px;height:7px;border-radius:50%;border:1px solid #888;background:#ccc}
.dot.on{background:var(--blue);box-shadow:inset 0 0 0 1.5px #fff}

/* main table */
.progress-panel{position:absolute;left:142px;top:52px;width:1040px;height:292px;background:var(--white);border:1px solid var(--border)}
.grid{display:grid;grid-template-columns:59px 59px 60px 59px 59px 60px 59px 59px 55px 55px 55px 55px 58px 58px 58px 59px 59px;column-gap:3px;padding-left:1px}
.thead{grid-template-rows:10px 10px 10px;margin-top:1px}
.th{background:var(--blue);color:var(--white);font-size:5.3px;font-weight:700;line-height:5.5px;grid-row:1/4;display:flex;align-items:center;padding-left:8px}
.th.top{align-items:flex-start;padding-top:3px}
.th.sub{grid-row:auto;justify-content:center;align-items:center;border:1px solid var(--white);padding:0}
.th.sub.left{justify-content:flex-start;padding-left:6px}
.th.last{font-size:6.5px;font-weight:500}
.tr{height:30px;align-items:center;font-size:5.3px;color:var(--text-blue)}
.tr.band{background:var(--band)}
.tr > span{padding-left:7px;white-space:nowrap}
.tr .c{padding-left:0;text-align:center}
.red{color:var(--red)}
.ok{color:var(--dark)}
.green{color:var(--green)}
.tr svg{display:block;margin:0 auto}

/* summary table */
.summary{position:absolute;left:144px;top:366px;width:421px;height:280px;background:var(--white)}
.sum-head{display:grid;grid-template-columns:209px 209px;column-gap:3px}
.sum-head div,.sum-sub div{background:var(--blue);color:var(--white);font-size:6.5px;font-weight:500;display:flex;align-items:center;justify-content:center}
.sum-head div{height:25px}
.sum-sub{display:grid;grid-template-columns:93px 113px 93px 113px;column-gap:3px;margin-top:2px}
.sum-sub div{height:25px}
.sum-row{display:grid;grid-template-columns:93px 113px 93px 113px;column-gap:3px;font-size:6.5px;color:var(--text-blue);align-items:center;text-align:center}
.sum-row.band{background:var(--band)}
</style>
</head>
<body>
<h1 class="page-title">Education Data Dashboard</h1>

<aside class="filters">
  <div class="field" style="top:0">
    <div class="field-inner">Enter student name
      <svg width="8" height="8" viewBox="0 0 10 10"><circle cx="4" cy="4" r="3" fill="none" stroke="#1e88e5" stroke-width="1.4"/><line x1="6.2" y1="6.2" x2="9" y2="9" stroke="#1e88e5" stroke-width="1.6"/></svg>
    </div>
  </div>
  <div class="filter-label" style="top:32px">Filter by School...</div>
  <div class="field" style="top:46px"><div class="field-inner">Select school.... <span class="caret"></span></div></div>
  <div class="radios"><span class="radio"><span class="dot on"></span>Observer</span><span class="radio"><span class="dot"></span>Teacher</span></div>
  <div class="field" style="top:90px"><div class="field-inner">Select observer <span class="caret"></span></div></div>
  <div class="filter-label" style="top:118px;left:3px">From:</div>
  <div class="field" style="top:131px"><div class="field-inner">02-04-2018
    <svg width="8" height="8" viewBox="0 0 10 10"><rect x="1" y="2" width="8" height="7" fill="none" stroke="#1e88e5" stroke-width="1.2"/><rect x="1" y="2" width="8" height="2" fill="#1e88e5"/></svg></div></div>
  <div class="filter-label" style="top:156px;left:3px">To:</div>
  <div class="field" style="top:169px"><div class="field-inner">09-04-2018.
    <svg width="8" height="8" viewBox="0 0 10 10"><rect x="1" y="2" width="8" height="7" fill="none" stroke="#1e88e5" stroke-width="1.2"/><rect x="1" y="2" width="8" height="2" fill="#1e88e5"/></svg></div></div>
</aside>

<section class="progress-panel">
  <div class="grid thead">
    <div class="th" style="grid-column:1">Name</div>
    <div class="th" style="grid-column:2;padding-left:20px">Observer</div>
    <div class="th" style="grid-column:3;padding-left:22px">School</div>
    <div class="th top" style="grid-column:4">Course Title</div>
    <div class="th top" style="grid-column:5;padding-left:18px">Current<br>Grade</div>
    <div class="th" style="grid-column:6;padding-left:28px">Raw<br>Score</div>
    <div class="th top" style="grid-column:7;padding-left:16px">Couser<br>Start<br>Date</div>
    <div class="th top" style="grid-column:8">Course<br>End<br>Date</div>
    <div class="th sub" style="grid-column:9/13;grid-row:1">Percent Complete</div>
    <div class="th sub" style="grid-column:9/11;grid-row:2">START – 2/27/18</div>
    <div class="th sub" style="grid-column:11/13;grid-row:2">END – 3/6/18</div>
    <div class="th sub left" style="grid-column:9;grid-row:3">Actual %</div>
    <div class="th sub left" style="grid-column:10;grid-row:3;padding-left:10px">Goal %</div>
    <div class="th sub left" style="grid-column:11;grid-row:3;padding-left:24px">Actual %</div>
    <div class="th sub left" style="grid-column:12;grid-row:3;padding-left:18px">Goal %</div>
    <div class="th" style="grid-column:13;padding-left:12px">2/27-3/6<br>Progress<br>Actual/ Goal</div>
    <div class="th top" style="grid-column:14;padding-left:10px;padding-top:7px">Status as of<br>March 6</div>
    <div class="th" style="grid-column:15;padding-left:10px">Completion<br>Rate / day<br>for the range</div>
    <div class="th" style="grid-column:16;padding-left:11px">Completion<br>Rate Change</div>
    <div class="th last" style="grid-column:17;padding-left:12px">Last Login</div>
  </div>

  <div class="grid tr">
    <span>Adrian Moles</span><span>Sal Cote</span><span>Rosewood</span><span>Algebra 1A</span><span>67.3 %</span><span>70 %</span><span>2/20/18</span><span>4/24/18</span><span>0%</span><span class="c">10%</span><span class="c">5%</span><span class="c">20%</span><span class="c red">5/10</span><span class="c red">5/20</span><span class="c">2%</span><span><svg width="12" height="8"><polygon points="6,0 12,8 0,8" fill="#1b7a1b"/></svg></span><span>3/6/18</span>
  </div>
  <div class="grid tr band">
    <span>Jorge Alvaro</span><span>Sal Cote</span><span>Rosewood</span><span>Biology A</span><span>74.2%</span><span>83%</span><span>2/20/18</span><span>4/24/18</span><span>5%</span><span class="c">10%</span><span class="c">15%</span><span class="c">20%</span><span class="c ok">10/10</span><span class="c red">5/20</span><span class="c">2.28%</span><span><svg width="12" height="8"><polygon points="6,0 12,8 0,8" fill="#1b7a1b"/></svg></span><span>3/6/18</span>
  </div>
  <div class="grid tr">
    <span>Mara Leone</span><span>Jena Intorre</span><span>Kendrick</span><span>US History A</span><span>82.3%</span><span>82.3%</span><span>2/20/18</span><span>4/24/18</span><span>15%</span><span class="c">10%</span><span class="c">20%</span><span class="c">20%</span><span class="c red">5/10</span><span class="c green">20/20</span><span class="c">7.14%</span><span><svg width="12" height="8"><polygon points="0,0 12,0 6,8" fill="#c62828"/></svg></span><span>3/3/18</span>
  </div>
  <div class="grid tr band">
    <span>Marco Smeed</span><span>Jena Intorre</span><span>Kendrick</span><span>Algebra 1A</span><span>91.0%</span><span>95.0%</span><span>2/20/18</span><span>4/24/18</span><span>9%</span><span class="c">10%</span><span class="c">11%</span><span class="c">20%</span><span class="c red">2/10</span><span class="c red">11/20</span><span class="c">5%</span><span><svg width="12" height="8"><polygon points="0,0 12,0 6,8" fill="#c62828"/></svg></span><span>3/3/18</span>
  </div>
  <div class="grid tr">
    <span>Julio Roderick</span><span>Meg Jansen</span><span>Birchbank</span><span>Language Arts 10B</span><span>94.5%</span><span>94.5%</span><span>2/20/18</span><span>4/24/18</span><span>11%</span><span class="c">10%</span><span class="c">28%</span><span class="c">20%</span><span class="c ok">17/10</span><span class="c ok">28/20</span><span class="c">2.8%</span><span><svg width="12" height="8"><polygon points="6,0 12,8 0,8" fill="#1b7a1b"/></svg></span><span>3/2/18</span>
  </div>
  <div class="grid tr band">
    <span>Jose Carmo</span><span>Meg Jansen</span><span>Birchbank</span><span>Language Arts 10B</span><span>80%</span><span>85%</span><span>2/20/18</span><span>4/24/18</span><span>5%</span><span class="c">10%</span><span class="c">10%</span><span class="c">20%</span><span class="c red">5/10</span><span class="c red">10/20</span><span class="c">3%</span><span><svg width="16" height="4"><rect width="16" height="4" fill="#222"/></svg></span><span>3/2/18</span>
  </div>
  <div class="grid tr">
    <span>Julia Carne</span><span>Meg Jansen</span><span>Birchbank</span><span>US History 1A</span><span>75%</span><span>80%</span><span>2/20/18</span><span>4/24/18</span><span>10%</span><span class="c">10%</span><span class="c">20%</span><span class="c">20%</span><span class="c ok">10/10</span><span class="c green">20/20</span><span class="c">2%</span><span><svg width="16" height="4"><rect width="16" height="4" fill="#222"/></svg></span><span>3/5/18</span>
  </div>
</section>

<section class="summary">
  <div class="sum-head"><div>START – 2/27/18</div><div>END – 3/6/18</div></div>
  <div class="sum-sub"><div>% complete</div><div>% complete Goal</div><div>% complete</div><div>% complete goal</div></div>
  <div class="sum-row" style="height:35px"><span>10%</span><span>10%</span><span>15%</span><span>20%</span></div>
  <div class="sum-row band" style="height:30px"><span>5%</span><span>50%</span><span>15%</span><span>20%</span></div>
  <div class="sum-row" style="height:32px"><span>15%</span><span>150%</span><span>20%</span><span>100%</span></div>
  <div class="sum-row band" style="height:31px"><span>9%</span><span>90%</span><span>11%</span><span>55%</span></div>
  <div class="sum-row" style="height:33px"><span>11%</span><span>110%</span><span>18%</span><span>90%</span></div>
  <div class="sum-row band" style="height:31px"></div>
</section>
</body>
</html>
```